New Software Development Firm Needs Stationery

Brindle Works, LLC is a new software development firm specializing in document management and custom engineering applications. We just completed a logo design project on PixelHarbor.

We also have an open project right now on PixelHarbor for business card design. ** We highly encourage you to submit designs to both projects as we want the two designs to have the same look and feel.

Design must be provided for coordinated letterhead and envelopes that works with the selected business card design on the other project.

We want a clean, professional and modern look that works well with our logo. We also require a recommendation for what PC font to use when printing on the new letterhead and envelopes.

The final submission must include source Photoshop or Illustrator files and any fonts used must be specified exactly.

Target Market(s)

Small to medium business professionals - including manufacturers, civil engineering firms, government agencies, architects, as well as general business.

Industry/Entity Type

Software

Requirements
Must have
• Must work very well with logo and business card design. Must work well with a specified and readily-available font on most PCs.
Nice to have
• White letterhead and envelopes are probably preferred, but we're open to suggestions!

```html
<!DOCTYPE html>
<html lang="en">
<head>
<meta charset="utf-8">
<title>Brindle Works, LLC – Envelope</title>
<link rel="stylesheet" href="https://fonts.googleapis.com/css2?family=Lato:ital,wght@0,400;0,700;1,400&display=swap">
<style>
  :root {
    --backdrop: #e9e7e3;
    --paper: #fbfbfa;
    --paper-edge: #dcdcda;
    --ink: #141414;
    --ink-soft: #3a3a3a;
    --accent: #d8222b;
  }
  * { box-sizing: border-box; margin: 0; padding: 0; }
  html, body {
    width: 1200px;
    height: 720px;
    overflow: hidden;
    background: var(--backdrop);
  }
  .canvas {
    width: 1200px;
    height: 720px;
    display: flex;
    align-items: center;
    justify-content: center;
  }
  .envelope {
    position: relative;
    width: 1000px;
    height: 470px;
    background: var(--paper);
    border: 1px solid var(--paper-edge);
    box-shadow: 0 8px 24px rgba(0, 0, 0, 0.12);
  }
  .sender {
    position: absolute;
    left: 64px;
    top: 46px;
  }
  .sender__name {
    font-family: "Lato", sans-serif;
    font-weight: 700;
    font-size: 48px;
    line-height: 1;
    letter-spacing: 0.5px;
    color: var(--ink);
  }
  .sender__block {
    display: flex;
    align-items: flex-start;
    gap: 12px;
    margin-top: 14px;
  }
  .sender__mark {
    width: 14px;
    height: 14px;
    margin-top: 2px;
    background: var(--accent);
    flex: none;
  }
  .sender__address {
    font-family: "Lato", sans-serif;
    font-style: italic;
    font-size: 12.5px;
    line-height: 1.3;
    color: var(--ink-soft);
  }
</style>
</head>
<body>
  <main class="canvas">
    <section class="envelope" aria-label="Brindle Works envelope">
      <header class="sender">
        <div class="sender__name">Brindle Works</div>
        <div class="sender__block">
          <span class="sender__mark"></span>
          <address class="sender__address">
            Brindle Works LLC<br>
            Calle Olmo 14, Col. Arboleda<br>
            The City DF 06210, MX<br>
            12345 The Country
          </address>
        </div>
      </header>
    </section>
  </main>
</body>
</html>
```